Pilates business needs a face list flyer

We are a pilates business that has been based in England for 15 years and looking for a new flyer that is eye catch and modern but stylish
we are trying to capture the male market as well as the female market so the leaflet should draw attention to both groups.
I have attached a copy of the literature needed on the flyer also a picture of its founder

Target Market(s)

market age group 18-70+ male and female

Industry/Entity Type

Business

Other font styles liked:
• calbri

Colors
33b8a4
34a7d8
3277b5
abd037

Requirements
Must have
• Literature attached
Nice to have
• To target both the male and female market. stylish but eye catching
Should not have
• pinks purples

```html
<!DOCTYPE html>
<html lang="en">
<head>
<meta charset="utf-8">
<title>Pilates Tri-fold Leaflet</title>
<link rel="stylesheet" href="https://fonts.googleapis.com/css2?family=Oswald:wght@300;400&family=Open+Sans:wght@400;600;700&display=swap">
<style>
:root{
  --teal:#33b8a4;
  --teal-dark:#1f9c8c;
  --sky:#34a7d8;
  --blue:#3277b5;
  --navy:#1d4f94;
  --lime:#abd037;
  --heading-green:#1f7a5c;
  --ink:#2b2b2b;
  --paper:#ffffff;
  --page:#e8e8e8;
}
*{margin:0;padding:0;box-sizing:border-box}
html,body{width:848px;height:1200px;overflow:hidden;background:var(--page)}
body{position:relative;font-family:"Open Sans",Arial,sans-serif;color:var(--ink)}
.sheet{position:absolute;left:48px;width:752px;height:585px;background:var(--paper);overflow:hidden;box-shadow:0 1px 4px rgba(0,0,0,.15)}
.sheet--outside{top:10px}
.sheet--inside{top:605px}
.fold{position:absolute;top:0;bottom:0;width:251px}
.fold--shade{background:linear-gradient(90deg,rgba(0,0,0,.035),rgba(0,0,0,0) 20%,rgba(0,0,0,0) 85%,rgba(0,0,0,.05))}
.waves{position:absolute;left:0;top:0;width:752px;height:585px}
.abs{position:absolute}
.photo{position:absolute}

/* schedule */
.schedule{left:0;top:22px;width:251px;text-align:center}
.session{margin-bottom:9px}
.session__time{font-size:10px;font-weight:700;color:var(--blue);line-height:13px}
.session__venue{font-size:8.6px;color:var(--ink);line-height:11px}
.circle-photo{position:absolute;border-radius:50%;border:5px solid var(--blue);box-shadow:0 0 0 3px #fff}

/* about */
.section-title{font-family:"Oswald",Arial,sans-serif;font-weight:300;color:var(--blue);font-size:16px;line-height:20px;letter-spacing:.2px;text-transform:uppercase}
.about-title{left:276px;top:16px;width:214px;display:flex;align-items:center;gap:10px;font-size:14px}
.about-title::after{content:"";flex:1;height:3px;background:var(--blue)}
.about-portrait{left:276px;top:48px;width:76px;height:88px;background:linear-gradient(160deg,#d9d9d9,#9a9a9a)}
.body-text{font-size:7.7px;line-height:11.2px;color:var(--ink);text-align:justify}
.body-text p{margin-bottom:6px}
.about-intro{left:360px;top:46px;width:130px}
.about-rest{left:276px;top:146px;width:214px}
.call{left:251px;top:400px;width:251px;text-align:center;font-family:"Oswald",Arial,sans-serif;font-weight:300;font-size:22px;color:var(--blue)}
.web{left:251px;width:251px;text-align:center;font-size:9.5px;letter-spacing:3px;color:var(--ink)}
.brand{text-align:center;font-family:"Oswald",Arial,sans-serif;font-weight:300;line-height:1.1}
.brand--cover{left:502px;top:36px;width:250px;font-size:32px;color:#555}
.brand--cover .brand__mark{color:var(--blue)}
.brand--inside{left:258px;top:20px;width:250px;font-size:23px;color:#fff}

/* inside */
.col{position:absolute;top:190px}
.col--one{left:22px;width:218px}
.col--two{left:276px;width:214px}
.col--three{left:522px;width:212px;top:184px}
.sub-title{font-size:12.5px;line-height:16px;font-weight:700;color:var(--heading-green);margin:8px 0 5px}
.benefits{list-style:none;font-size:7.7px;line-height:11.2px;color:var(--ink)}
.benefits li{position:relative;padding-left:9px}
.benefits li::before{content:"";position:absolute;left:1px;top:4.5px;width:3.5px;height:3.5px;border-radius:50%;background:var(--sky)}
</style>
</head>
<body>

<section class="sheet sheet--outside">
  <div class="photo" role="img" aria-label="Photo of a woman in a white dress with arms open on a bright beach" style="left:502px;top:0;width:250px;height:585px;background:linear-gradient(180deg,#f3efe9 0%,#e8ddd0 45%,#d9c8b4 75%,#cdbba5 100%)"></div>
  <div class="photo" role="img" aria-label="Faint background photo of a person stretching" style="left:251px;top:360px;width:251px;height:160px;background:linear-gradient(180deg,rgba(230,230,230,0),rgba(215,215,215,.7))"></div>
  <div class="fold fold--shade" style="left:0"></div>
  <div class="fold fold--shade" style="left:251px"></div>

  <div class="abs schedule">
    <div class="session"><div class="session__time">Monday 10.30pm Beginner-Improver</div><div class="session__venue">The Meadow Hall, Mill Lane, Ashwick</div></div>
    <div class="session"><div class="session__time">Monday 11.30pm Small group Class.</div><div class="session__venue">The Meadow Hall, Mill Lane, Ashwick</div></div>
    <div class="session"><div class="session__time">Monday 6.45pm Progressive-Intermediate+</div><div class="session__venue">St Aldric Sch, The Orchards, Fernley</div></div>
    <div class="session"><div class="session__time">Monday 7.45pm Beginner-Improver</div><div class="session__venue">St Aldric Sch, The Orchards, Fernley</div></div>
    <div class="session"><div class="session__time">Tuesday 5.45pm Small group class</div><div class="session__venue">The Oak Centre, Elm Rd, Brookham</div></div>
    <div class="session"><div class="session__time">Tuesday 6.45pm Beginner-Improver</div><div class="session__venue">The Oak Centre, Elm Rd, Brookham</div></div>
    <div class="session"><div class="session__time">Wednesday 10am Progressive</div><div class="session__venue">The Oak Centre, Elm Rd, Brookham</div></div>
    <div class="session"><div class="session__time">Wednesday 11am Beginners</div><div class="session__venue">The Oak Centre, Elm Rd, Brookham</div></div>
    <div class="session"><div class="session__time">Wednesday 6.45pm<br>Beginner-Progressive Holtby,</div><div class="session__venue">Village Hall, Green St, Holtby, Nr Harwell</div></div>
    <div class="session"><div class="session__time">Thursday 10am Beginner-Progressive</div><div class="session__venue">Church Rooms, High St, Fernley</div></div>
    <div class="session"><div class="session__time">Thursday 6.30pm Progressive-</div><div class="session__venue">The Meadow Hall, Mill Lane, Ashwick</div></div>
    <div class="session"><div class="session__time">Thursday 7.30pm Beginner-Progressive</div><div class="session__venue">The Meadow Hall, Mill Lane, Ashwick</div></div>
  </div>

  <svg class="waves" viewBox="0 0 752 585" aria-hidden="true">
    <path d="M0,505 C150,495 300,510 430,545 C560,578 680,560 752,540 L752,585 L0,585 Z" fill="var(--teal)"/>
    <path d="M240,478 C360,480 460,520 560,540 C650,556 710,535 752,515 L752,552 C690,572 610,580 540,572 C430,560 330,505 240,492 Z" fill="var(--navy)"/>
    <path d="M240,470 C360,472 460,508 560,522 C640,532 700,505 752,478 L752,490 C700,518 640,544 560,534 C460,520 360,484 240,480 Z" fill="var(--lime)"/>
  </svg>

  <div class="circle-photo" role="img" aria-label="Photo of a woman doing yoga on rocks by the sea" style="left:22px;top:445px;width:112px;height:112px;background:linear-gradient(180deg,#bfe1f0,#9fc4d4 60%,#c9c2b5)"></div>
  <div class="circle-photo" role="img" aria-label="Photo of a man and woman stretching on a beach" style="left:138px;top:432px;width:106px;height:106px;background:linear-gradient(180deg,#9fd6ec,#7fb7cf 55%,#d9c8b0)"></div>

  <h2 class="abs section-title about-title">About Maren</h2>
  <div class="photo about-portrait" role="img" aria-label="Portrait photo of founder Maren"></div>
  <div class="abs body-text about-intro"><p>Maren is a one of the most experienced and a leading Pilates teacher in the Midlands. She has been studying and working within the fitness industry for 20 years. Since 1992 she has specialized in aerobics, dance and other studio-based classes.</p></div>
  <div class="abs body-text about-rest">
    <p>In 1999, Maren received her first degree in Sport and Leisure from the Westbrook University.In 2000 she became the studio aerobic and fitness programmecoordinator for the largest sportscentre in England</p>
    <p>2001 saw Maren studying and complete, a Diploma in Pilates with Daniel Ross, London. In 2002, Maren established Midland Core Pilates which bases its teaching practice on a Pilates method combining up to date knowledge of exercise physiology and techniques; whilst retaining the authentic concept of its founder the method's founder. For the past 10 years Maren has taught Pilates locally, nationally and internationally.</p>
    <p>Since Maren 2006 Maren has continued with her professional development and studiedOsteopathy, Traditional Acupuncture at Riverside College and Tai Chi.Thiswealth of knowledge and comprehensiveskill-base brings a unique richness to her classes and private sessions.</p>
  </div>
  <div class="abs call">CALL: 1234567890</div>
  <div class="abs web" style="top:442px">www.yourwebsite.com</div>

  <div class="abs brand brand--cover"><div class="brand__mark">LOGO</div><div>COMPANY NAME</div></div>
</section>

<section class="sheet sheet--inside">
  <div class="photo" role="img" aria-label="Faint background photo of a woman relaxing" style="left:502px;top:100px;width:250px;height:340px;background:linear-gradient(180deg,rgba(235,225,215,.0),rgba(230,218,205,.55) 50%,rgba(235,225,215,0))"></div>
  <div class="fold fold--shade" style="left:0"></div>
  <div class="fold fold--shade" style="left:251px"></div>
  <div class="photo" role="img" aria-label="Photo of a man in a blue vest doing a stretch on a beach" style="left:0;top:0;width:258px;height:175px;background:linear-gradient(180deg,#9ed3ee 0%,#bfe3f2 45%,#78b7c6 62%,#8db86a 100%)"></div>

  <svg class="waves" viewBox="0 0 752 585" aria-hidden="true">
    <rect x="258" y="0" width="494" height="120" fill="var(--teal)"/>
    <path d="M258,120 C400,130 560,70 752,30 L752,60 C600,90 420,150 258,150 Z" fill="var(--teal)"/>
    <path d="M60,130 C200,175 360,165 520,100 C620,60 700,40 752,34 L752,70 C680,80 600,110 520,130 C380,185 200,190 60,150 Z" fill="var(--navy)"/>
    <path d="M0,112 C120,165 260,185 420,160 C560,138 660,100 752,84 L752,98 C660,115 560,152 420,175 C260,200 120,182 0,130 Z" fill="var(--lime)"/>
    <path d="M0,135 C120,185 260,205 420,180 C560,158 660,120 752,104 L752,110 C660,126 560,166 420,188 C260,212 120,195 0,150 Z" fill="#fff"/>
  </svg>
  <div class="abs brand brand--inside"><div>LOGO</div><div>COMPANY NAME</div></div>

  <div class="col col--one">
    <h2 class="section-title">What is Pilates?</h2>
    <div class="body-text" style="margin-top:8px">
      <p>Pilates is now the hottest and most talked about fitness trend since the aerobic explosion of the past 30 years. A perfect blend of Eastern and Western philosophy. Pilates is a holistic approach to exercise, that integrates body and mind. It concentrates on building strength stamina balance and co-ordination, improving flexibility coordination posture, breathing and well-being.</p>
    </div>
    <h3 class="sub-title">Classes</h3>
    <div class="body-text">
      <p>All classes are based upon the original 34 movements developed by the method's founder. Classes provide low impact yet highly intense workouts, ideal for everyone, whatever age or ability or whether the individual is fit, sedentary or recuperating after illness or surgery. Furthermore, Pilates provides a safe and beneficial workout for expectant and new mothers.</p>
      <p>Each session is designed to,</p>
    </div>
    <ul class="benefits">
      <li>change the way you look</li>
      <li>create lean muscles</li>
      <li>Increase strength, flexibility, coordination and proper body alignment</li>
      <li>Increase core strength</li>
      <li>Reduce fatigue, stress and risk of injury</li>
      <li>Reduce back and joint pain</li>
      <li>Rehabilitation</li>
      <li>Increase circulation</li>
      <li>Improve body mind integration</li>
    </ul>
  </div>

  <div class="col col--two">
    <h2 class="section-title">Class Description</h2>
    <h3 class="sub-title" style="margin-top:12px">Small Group Pilates (new)</h3>
    <div class="body-text"><p>This class is Structure similar to a private session. Max of 6 people allows movement plans to be more tailored to individual's needs then a larger group class. Will take from the basics and help to build on these skills to improve posture and to develop strength and flexibility. Home plan provided</p></div>
    <h3 class="sub-title">Beginner-Improvers</h3>
    <div class="body-text"><p>Ideal for those new to the Pilates technique. In this programme you will develop an understanding of the principals, gain strength, stamina and flexibility safely, as you are guided through a series of beginner movements, modified and tailored to your own needs and ability.</p></div>
    <h3 class="sub-title">Beginner-Improvers</h3>
    <div class="body-text"><p>Ideal stepping stone from beginners building on moves that you have already learnt at a more intense level, as well as learning new moves. Incorporating small equipment such as the isotoner, the stability ball, roller and Pilates balance weights to help increase the intensity of the workout without it being over challenging for those still developing their skill base.</p></div>
  </div>
  <div class="abs web" style="top:553px">www.yourwebsite.com</div>

  <div class="col col--three">
    <h3 class="sub-title" style="margin-top:0">Intermediate-Advanced</h3>
    <div class="body-text"><p>This class is designed for those already well versed in the Pilates technique. Both physically and mentally challenging, new movements are incorporated with combinations and higher intensityof known movements, alongside with the use of small equipment</p></div>
    <h2 class="section-title" style="margin-top:6px">Private Sessions</h2>
    <div class="body-text" style="margin-top:6px">
      <p style="margin-bottom:0">Perfect for anyone with specific needs, restricted time frame, or limited ability.Sessions are built using the 8 Pilates principals and designed to encompass all your individual needs, with the focus upon restoring strength, flexibility, equilibrium and well being. Continued support and home movement plans are provided to help motivate and to help with achieving your goals</p>
      <p style="margin-bottom:0">Your private session can be arranged in the convenience of your own home or a location near to you. Please contact Maren for further details and availability.</p>
    </div>
  </div>

  <div class="photo" role="img" aria-label="Photo of a group exercising on mats in a Pilates class" style="left:508px;top:450px;width:244px;height:135px;background:linear-gradient(135deg,#e4e4e4,#b9b9b9 50%,#7d8a96)"></div>
  <svg class="abs" style="left:508px;top:450px" width="244" height="40" viewBox="0 0 244 40" aria-hidden="true">
    <path d="M0,0 L244,0 L244,30 C170,8 80,4 0,14 Z" fill="#fff"/>
    <path d="M0,14 C80,4 170,8 244,30 L244,36 C170,14 80,10 0,20 Z" fill="var(--navy)"/>
  </svg>
</section>

</body>
</html>
```